Feeling Wheel Infographic

We need the 2 pptx mock-ups turned to 2 infographics. please add the logo to the infographics. The colours used on the mock-ups are example colours and can be changed - a gradient scale or the colours used on the mock-up would be great!

```html
<!DOCTYPE html>
<html lang="en">
<head>
<meta charset="utf-8">
<title>Feeling Wheel Infographic</title>
<link href="https://fonts.googleapis.com/css2?family=Montserrat:wght@300;400;700;800&display=swap" rel="stylesheet">
<style>
  :root {
    --ink: #111111;
    --muted: #4a4a4a;
    --paper: #ffffff;
    --proud: #e8222d;     --proud-soft: #f27b80;
    --joyful: #f15a24;    --joyful-soft: #f7966f;
    --intrigued: #f7931e; --intrigued-soft: #fbbf73;
    --trusting: #fbb03b;  --trusting-soft: #fdd38c;
    --loving: #f9e400;    --loving-soft: #fcf07a;
    --peaceful: #8cc63f;  --peaceful-soft: #b9dc88;
    --ashamed: #39b54a;   --ashamed-soft: #86d38f;
    --sad: #1fa89a;       --sad-soft: #75cbc1;
    --surprised: #29abe2; --surprised-soft: #80ccee;
    --afraid: #1e6fbf;    --afraid-soft: #6fa4d9;
    --disgusted: #662d91; --disgusted-soft: #9d77bb;
    --angry: #92278f;     --angry-soft: #bf78bd;
  }
  html, body { margin: 0; padding: 0; overflow: hidden; }
  body { background: #e9e9e9; }
  .canvas {
    position: relative; width: 1200px; height: 1000px; overflow: hidden;
    background: radial-gradient(circle at 70% 45%, #ffffff 0%, #ffffff 55%, #f3f3f3 100%);
    font-family: "Montserrat", sans-serif;
  }
  .title { position: absolute; left: 52px; top: 48px; margin: 0; line-height: 1; }
  .title-main { display: block; font-weight: 800; font-size: 36px; color: var(--ink); letter-spacing: 0.5px; }
  .title-sub { display: block; font-weight: 300; font-size: 34px; color: var(--muted); letter-spacing: 2px; margin-top: 4px; }
  .wheel { position: absolute; left: 0; top: 0; }
  .petal { fill: var(--c); stroke: var(--paper); stroke-width: 6; stroke-linejoin: round; }
  .petal-label { font-family: "Montserrat", sans-serif; font-weight: 800; font-size: 21px; fill: #fff; text-anchor: middle; dominant-baseline: central; }
  .icon-disc { fill: #fff; }
  .band { fill: none; stroke: #fff; stroke-opacity: 0.22; stroke-width: 40; }
  .hub-ring { fill: #fff; }
  .sector-outer { fill: var(--c); stroke: #fff; stroke-width: 2; }
  .sector-inner { fill: var(--s); stroke: #fff; stroke-width: 2; }
  .words { font-family: "Montserrat", sans-serif; font-weight: 700; text-anchor: middle; dominant-baseline: central; }
  .words-outer { font-size: 11.5px; fill: #fff; }
  .words-inner { font-size: 8px; fill: #fff; }
  .dark .words-outer, .dark .words-inner { fill: #1a1a1a; }
  .proud { --c: var(--proud); --s: var(--proud-soft); }
  .joyful { --c: var(--joyful); --s: var(--joyful-soft); }
  .intrigued { --c: var(--intrigued); --s: var(--intrigued-soft); }
  .trusting { --c: var(--trusting); --s: var(--trusting-soft); }
  .loving { --c: var(--loving); --s: var(--loving-soft); }
  .peaceful { --c: var(--peaceful); --s: var(--peaceful-soft); }
  .ashamed { --c: var(--ashamed); --s: var(--ashamed-soft); }
  .sad { --c: var(--sad); --s: var(--sad-soft); }
  .surprised { --c: var(--surprised); --s: var(--surprised-soft); }
  .afraid { --c: var(--afraid); --s: var(--afraid-soft); }
  .disgusted { --c: var(--disgusted); --s: var(--disgusted-soft); }
  .angry { --c: var(--angry); --s: var(--angry-soft); }
</style>
</head>
<body>
<div class="canvas">
  <h1 class="title"><span class="title-main">FEELING WHEEL</span><span class="title-sub">INFOGRAPHIC</span></h1>

  <svg class="wheel" width="1200" height="1000" viewBox="0 0 1200 1000">
    <defs>
      <path id="petal-shape" d="M-50.1,-193.6 L-86.4,-334 L0,-395 L86.4,-334 L50.1,-193.6 Z"/>
      <path id="sector-outer" d="M-54.35,-202.85 A210,210 0 0 1 54.35,-202.85 L28.47,-106.25 A110,110 0 0 0 -28.47,-106.25 Z"/>
      <path id="sector-inner" d="M-28.47,-106.25 A110,110 0 0 1 28.47,-106.25 L12.42,-46.36 A48,48 0 0 0 -12.42,-46.36 Z"/>
      <filter id="hub-shadow" x="-20%" y="-20%" width="140%" height="140%">
        <feDropShadow dx="0" dy="2" stdDeviation="4" flood-opacity="0.18"/>
      </filter>
    </defs>

    <g transform="translate(600,520)">
      <g class="petals">
        <use href="#petal-shape" class="petal proud" transform="rotate(15)"/>
        <use href="#petal-shape" class="petal joyful" transform="rotate(45)"/>
        <use href="#petal-shape" class="petal intrigued" transform="rotate(75)"/>
        <use href="#petal-shape" class="petal trusting" transform="rotate(105)"/>
        <use href="#petal-shape" class="petal loving" transform="rotate(135)"/>
        <use href="#petal-shape" class="petal peaceful" transform="rotate(165)"/>
        <use href="#petal-shape" class="petal ashamed" transform="rotate(195)"/>
        <use href="#petal-shape" class="petal sad" transform="rotate(225)"/>
        <use href="#petal-shape" class="petal surprised" transform="rotate(255)"/>
        <use href="#petal-shape" class="petal afraid" transform="rotate(285)"/>
        <use href="#petal-shape" class="petal disgusted" transform="rotate(315)"/>
        <use href="#petal-shape" class="petal angry" transform="rotate(345)"/>
      </g>

      <circle class="band" r="250"/>

      <g class="icons">
        <circle class="icon-disc" role="img" aria-label="Proud emotion icon" r="24" transform="rotate(15) translate(0,-272)"/>
        <circle class="icon-disc" role="img" aria-label="Joyful emotion icon" r="24" transform="rotate(45) translate(0,-272)"/>
        <circle class="icon-disc" role="img" aria-label="Intrigued emotion icon" r="24" transform="rotate(75) translate(0,-272)"/>
        <circle class="icon-disc" role="img" aria-label="Trusting emotion icon" r="24" transform="rotate(105) translate(0,-272)"/>
        <circle class="icon-disc" role="img" aria-label="Loving emotion icon" r="24" transform="rotate(135) translate(0,-272)"/>
        <circle class="icon-disc" role="img" aria-label="Peaceful emotion icon" r="24" transform="rotate(165) translate(0,-272)"/>
        <circle class="icon-disc" role="img" aria-label="Ashamed emotion icon" r="24" transform="rotate(195) translate(0,-272)"/>
        <circle class="icon-disc" role="img" aria-label="Sad emotion icon" r="24" transform="rotate(225) translate(0,-272)"/>
        <circle class="icon-disc" role="img" aria-label="Surprised emotion icon" r="24" transform="rotate(255) translate(0,-272)"/>
        <circle class="icon-disc" role="img" aria-label="Afraid emotion icon" r="24" transform="rotate(285) translate(0,-272)"/>
        <circle class="icon-disc" role="img" aria-label="Disgusted emotion icon" r="24" transform="rotate(315) translate(0,-272)"/>
        <circle class="icon-disc" role="img" aria-label="Angry emotion icon" r="24" transform="rotate(345) translate(0,-272)"/>
      </g>

      <g class="labels">
        <text class="petal-label" transform="rotate(15) translate(0,-326)">PROUD</text>
        <text class="petal-label" transform="rotate(45) translate(0,-326)">JOYFUL</text>
        <text class="petal-label" transform="rotate(75) translate(0,-326)">INTRIGUED</text>
        <text class="petal-label" transform="rotate(105) translate(0,-326)">TRUSTING</text>
        <text class="petal-label" transform="rotate(135) translate(0,-326) rotate(180)">LOVING</text>
        <text class="petal-label" transform="rotate(165) translate(0,-326) rotate(180)">PEACEFUL</text>
        <text class="petal-label" transform="rotate(195) translate(0,-326) rotate(180)">ASHAMED</text>
        <text class="petal-label" transform="rotate(225) translate(0,-326) rotate(180)">SAD</text>
        <text class="petal-label" transform="rotate(255) translate(0,-326)">SURPRISED</text>
        <text class="petal-label" transform="rotate(285) translate(0,-326)">AFRAID</text>
        <text class="petal-label" transform="rotate(315) translate(0,-326)">DISGUSTED</text>
        <text class="petal-label" transform="rotate(345) translate(0,-326)">ANGRY</text>
      </g>

      <circle class="hub-ring" r="226" filter="url(#hub-shadow)"/>

      <g class="hub-sectors">
        <g class="proud"><use href="#sector-outer" class="sector-outer" transform="rotate(15)"/><use href="#sector-inner" class="sector-inner" transform="rotate(15)"/></g>
        <g class="joyful"><use href="#sector-outer" class="sector-outer" transform="rotate(45)"/><use href="#sector-inner" class="sector-inner" transform="rotate(45)"/></g>
        <g class="intrigued"><use href="#sector-outer" class="sector-outer" transform="rotate(75)"/><use href="#sector-inner" class="sector-inner" transform="rotate(75)"/></g>
        <g class="trusting"><use href="#sector-outer" class="sector-outer" transform="rotate(105)"/><use href="#sector-inner" class="sector-inner" transform="rotate(105)"/></g>
        <g class="loving"><use href="#sector-outer" class="sector-outer" transform="rotate(135)"/><use href="#sector-inner" class="sector-inner" transform="rotate(135)"/></g>
        <g class="peaceful"><use href="#sector-outer" class="sector-outer" transform="rotate(165)"/><use href="#sector-inner" class="sector-inner" transform="rotate(165)"/></g>
        <g class="ashamed"><use href="#sector-outer" class="sector-outer" transform="rotate(195)"/><use href="#sector-inner" class="sector-inner" transform="rotate(195)"/></g>
        <g class="sad"><use href="#sector-outer" class="sector-outer" transform="rotate(225)"/><use href="#sector-inner" class="sector-inner" transform="rotate(225)"/></g>
        <g class="surprised"><use href="#sector-outer" class="sector-outer" transform="rotate(255)"/><use href="#sector-inner" class="sector-inner" transform="rotate(255)"/></g>
        <g class="afraid"><use href="#sector-outer" class="sector-outer" transform="rotate(285)"/><use href="#sector-inner" class="sector-inner" transform="rotate(285)"/></g>
        <g class="disgusted"><use href="#sector-outer" class="sector-outer" transform="rotate(315)"/><use href="#sector-inner" class="sector-inner" transform="rotate(315)"/></g>
        <g class="angry"><use href="#sector-outer" class="sector-outer" transform="rotate(345)"/><use href="#sector-inner" class="sector-inner" transform="rotate(345)"/></g>
      </g>

      <circle class="hub-ring" r="46"/>

      <g class="hub-words">
        <g transform="rotate(-75)">
          <text class="words words-outer"><tspan x="158" y="-13">Brave</tspan><tspan x="158" y="0">Empowered</tspan><tspan x="158" y="13">Fulfilled</tspan></text>
          <text class="words words-inner"><tspan x="79" y="-5">Confident</tspan><tspan x="79" y="5">Encouraged</tspan></text>
        </g>
        <g transform="rotate(-45)">
          <text class="words words-outer"><tspan x="158" y="-13">Ecstatic</tspan><tspan x="158" y="0">Elated</tspan><tspan x="158" y="13">Thrilled</tspan></text>
          <text class="words words-inner"><tspan x="79" y="-5">Excited</tspan><tspan x="79" y="5">Happy</tspan></text>
        </g>
        <g transform="rotate(-15)" class="dark">
          <text class="words words-outer"><tspan x="158" y="-13">Fascinated</tspan><tspan x="158" y="0">Invested</tspan><tspan x="158" y="13">Captivated</tspan></text>
          <text class="words words-inner"><tspan x="79" y="-5">Engaged</tspan><tspan x="79" y="5">Curious</tspan></text>
        </g>
        <g transform="rotate(15)" class="dark">
          <text class="words words-outer"><tspan x="158" y="-13">Positive</tspan><tspan x="158" y="0">Certain</tspan><tspan x="158" y="13">Convinced</tspan></text>
          <text class="words words-inner"><tspan x="79" y="-5">Secure</tspan><tspan x="79" y="5">Optimistic</tspan></text>
        </g>
        <g transform="rotate(45)" class="dark">
          <text class="words words-outer"><tspan x="158" y="-13">Admiration</tspan><tspan x="158" y="0">Adoration</tspan><tspan x="158" y="13">Reverence</tspan></text>
          <text class="words words-inner"><tspan x="79" y="-5">Affectionate</tspan><tspan x="79" y="5">Connected</tspan></text>
        </g>
        <g transform="rotate(75)">
          <text class="words words-outer"><tspan x="158" y="-13">Tranquil</tspan><tspan x="158" y="0">Calm</tspan><tspan x="158" y="13">Satisfied</tspan></text>
          <text class="words words-inner"><tspan x="79" y="-5">Relaxed</tspan><tspan x="79" y="5">Content</tspan></text>
        </g>
        <g transform="rotate(285)">
          <text class="words words-outer"><tspan x="-158" y="-13">Mortified</tspan><tspan x="-158" y="0">Remorseful</tspan><tspan x="-158" y="13">Regretful</tspan></text>
          <text class="words words-inner"><tspan x="-79" y="-5">Embarrassed</tspan><tspan x="-79" y="5">Guilty</tspan></text>
        </g>
        <g transform="rotate(315)">
          <text class="words words-outer"><tspan x="-158" y="-13">Isolated</tspan><tspan x="-158" y="0">Powerless</tspan><tspan x="-158" y="13">Heartbroken</tspan></text>
          <text class="words words-inner"><tspan x="-79" y="-5">Lonely</tspan><tspan x="-79" y="5">Disappointed</tspan></text>
        </g>
        <g transform="rotate(345)">
          <text class="words words-outer"><tspan x="-158" y="-13">Stunned</tspan><tspan x="-158" y="0">Shocked</tspan><tspan x="-158" y="13">Startled</tspan></text>
          <text class="words words-inner"><tspan x="-79" y="-5">Confused</tspan><tspan x="-79" y="5">Amazed</tspan></text>
        </g>
        <g transform="rotate(15)">
          <text class="words words-outer"><tspan x="-158" y="-13">Worried</tspan><tspan x="-158" y="0">Frightened</tspan><tspan x="-158" y="13">Terrified</tspan></text>
          <text class="words words-inner"><tspan x="-79" y="-5">Scared</tspan><tspan x="-79" y="5">Nervous</tspan></text>
        </g>
        <g transform="rotate(45)">
          <text class="words words-outer"><tspan x="-158" y="-13">Mortified</tspan><tspan x="-158" y="0">Revolted</tspan><tspan x="-158" y="13">Repulsed</tspan></text>
          <text class="words words-inner"><tspan x="-79" y="-5">Appalled</tspan><tspan x="-79" y="5">Sickened</tspan></text>
        </g>
        <g transform="rotate(75)">
          <text class="words words-outer"><tspan x="-158" y="-13">Aggravated</tspan><tspan x="-158" y="0">Irritated</tspan><tspan x="-158" y="13">Jealous</tspan></text>
          <text class="words words-inner"><tspan x="-79" y="-5">Frustrated</tspan><tspan x="-79" y="5">Upset</tspan></text>
        </g>
      </g>
    </g>
  </svg>
</div>
</body>
</html>
```